Organization and people consulting firm needs a website design

I need a website that promotes and explains the consulting service we will provide. The organization is called Lakemont Counsel Group. Our services include organization design, employee experience, change management, and executive coaching. I would like to see a simple clean and professional design, that reflects a modern and forward looking professional services company

Target Market(s)

Mid market and large companies

Industry/Entity Type

Management Consulting

Coding

Coded - Design and coding required

Number of Pages Required

5+ page

Font styles to use
Sans Serif

Colors

Designer to choose colors to be used in the design.

Requirements
Must have
• The following pages: Home, The Way We Work, What We Do, Our Founder, Insights, Contact.
• Search button.
• Hyper links (will be provided with main body text)
• Scrolling website with summaries at top level and links to more detail at lower level (like this website: brightvane.com)
• Company logo (uploaded)
• I have text for each of the pages that I can upload once the basic design is done
Should not have
• No clutter, keep the design clean

```html
<!DOCTYPE html>
<html lang="en">
<head>
<meta charset="utf-8">
<title>Lakemont Counsel Group</title>
<link rel="stylesheet" href="https://fonts.googleapis.com/css2?family=Cinzel:wght@400;600;700&family=Open+Sans:ital,wght@0,400;0,600;0,700;1,400&display=swap">
<style>
:root{
  --red:#e3222f;
  --ink:#333333;
  --text:#3c3c3c;
  --muted:#6a6a6a;
  --band:#f3f3f3;
  --white:#ffffff;
  --footer:#6e6e6e;
  --hero-a:#c9d3dc;
  --hero-b:#8a98a8;
}
*{box-sizing:border-box;margin:0;padding:0}
html,body{width:1200px;height:2691px;overflow:hidden}
body{background:var(--white);color:var(--text);font-family:"Open Sans",Arial,sans-serif}

/* header */
.site-header{height:86px;display:flex;align-items:center;justify-content:space-between;padding:0 115px 0 111px}
.brand{font-family:"Cinzel",Georgia,serif;font-weight:700;font-size:17px;color:var(--red);display:flex;align-items:center;gap:8px;white-space:nowrap}
.brand-dot{width:12px;height:12px;border-radius:50%;background:var(--red);flex:none}
.main-nav{display:flex;align-items:center;gap:26px;white-space:nowrap}
.main-nav a{font-family:"Cinzel",Georgia,serif;font-size:13.5px;color:var(--ink);text-decoration:none}
.main-nav a.is-active{color:var(--red)}
.search-btn{width:30px;height:30px;background:var(--red);border-radius:3px;display:flex;align-items:center;justify-content:center}

/* hero */
.hero{height:474px;position:relative;background:linear-gradient(100deg,#2b2b30 0%,#4a4c55 28%,var(--hero-b) 45%,var(--hero-a) 70%,#e6ebef 100%)}
.hero-arrow{position:absolute;width:30px;height:40px}
.hero-arrow.prev{left:112px;top:200px}
.hero-arrow.next{left:1058px;top:216px}
.hero-brand{position:absolute;left:660px;top:330px;width:400px;text-align:center;font-family:"Cinzel",Georgia,serif;font-weight:700;color:var(--red);font-size:38px;line-height:1.1}

/* sections */
.section{text-align:center;overflow:hidden}
.section.alt{background:var(--band)}
.mark{width:14px;height:14px;border-radius:50%;background:var(--red);margin:0 auto}
.section-title{font-family:"Cinzel",Georgia,serif;font-weight:400;font-size:40px;line-height:40px;color:var(--ink);letter-spacing:1px}
.section-title b{font-weight:700}
.lead{font-size:15px;line-height:22px;color:var(--text);max-width:735px;margin:0 auto}
.btn{display:table;margin:0 auto;border:2px solid var(--red);border-radius:4px;font-family:"Cinzel",Georgia,serif;font-weight:600;font-size:13px;line-height:16px;color:var(--ink);padding:5px 18px;text-decoration:none;background:var(--white);letter-spacing:.5px}

.way{height:301px;padding-top:50px}
.way .section-title{margin-top:23px}
.way .lead{margin-top:14px}
.way .btn{margin-top:24px}

.services{height:423px;padding-top:48px}
.services .section-title{margin-top:19px}
.service-list{display:flex;justify-content:center;margin-top:46px}
.service{width:247px;display:flex;flex-direction:column;align-items:center}
.service svg{width:100px;height:100px}
.service-name{font-weight:700;font-size:19px;line-height:26px;color:var(--ink);margin-top:16px}
.service .btn{margin-top:21px;font-size:12px}

.founder{height:600px;padding-top:57px}
.founder .section-title{margin-top:19px}
.founder .lead{margin-top:23px}
.portrait{width:170px;height:194px;margin:20px auto 0;background:linear-gradient(180deg,#6b5b4e 0%,#3f3a38 55%,#2a2a2c 100%)}
.founder-name{font-family:"Cinzel",Georgia,serif;font-weight:700;font-size:22px;line-height:28px;color:var(--ink);margin-top:20px;letter-spacing:1px}
.founder-role{font-style:italic;font-size:14px;line-height:20px;color:var(--muted);margin-top:1px}
.founder .btn{margin-top:22px}

.insights{height:366px;padding-top:45px}
.insights .section-title{margin-top:20px}
.insights .lead{margin-top:23px;max-width:700px}
.subscribe{display:flex;justify-content:center;gap:16px;margin-top:31px}
.email-field{width:338px;height:30px;border:1px solid #dcdcdc;background:var(--white);display:flex;align-items:center;justify-content:space-between;padding:0 12px 0 22px;font-size:12px;color:var(--ink)}
.subscribe .btn{margin:0;padding:5px 22px}

.contact{height:319px;padding-top:69px}
.contact .section-title{margin-top:19px}
.contact .lead{margin-top:12px;max-width:700px}
.contact .btn{margin-top:26px;padding:5px 22px}

/* footer */
.site-footer{height:122px;background:var(--footer);position:relative;color:var(--white)}
.footer-nav{position:absolute;left:156px;top:26px;display:flex;gap:26px;white-space:nowrap}
.footer-nav a{font-family:"Cinzel",Georgia,serif;font-size:14px;line-height:20px;color:#f0f0f0;text-decoration:none}
.copyright{position:absolute;left:156px;top:62px;font-size:11px;color:#f0f0f0}
.follow{position:absolute;left:917px;top:24px}
.follow-title{font-family:"Cinzel",Georgia,serif;font-weight:700;font-size:15px;line-height:20px}
.social{display:flex;gap:5px;margin-top:10px;margin-left:-2px}
.social span{width:40px;height:40px;border-radius:50%;background:var(--white)}
</style>
</head>
<body>

<header class="site-header">
  <div class="brand"><span class="brand-dot"></span>Lakemont Counsel Group</div>
  <nav class="main-nav">
    <a href="#" class="is-active">Home</a>
    <a href="#">The Way We Work</a>
    <a href="#">What We Do</a>
    <a href="#">Our Founder</a>
    <a href="#">Insights</a>
    <a href="#">Contact</a>
    <span class="search-btn" aria-label="Search">
      <svg width="14" height="14" viewBox="0 0 14 14"><circle cx="6" cy="6" r="4" fill="none" stroke="#fff" stroke-width="2"/><line x1="9" y1="9" x2="13" y2="13" stroke="#fff" stroke-width="2"/></svg>
    </span>
  </nav>
</header>

<section class="hero" role="img" aria-label="Photograph of a consultant in conversation with a client in a bright office">
  <svg class="hero-arrow prev" viewBox="0 0 30 40"><polyline points="22,6 8,20 22,34" fill="none" stroke="#fff" stroke-width="6"/></svg>
  <svg class="hero-arrow next" viewBox="0 0 30 40"><polyline points="8,6 22,20 8,34" fill="none" stroke="#fff" stroke-width="6"/></svg>
  <div class="hero-brand">Lakemont<br>Counsel Group</div>
</section>

<section class="section way">
  <div class="mark"></div>
  <h2 class="section-title">The Way <b>We Work</b></h2>
  <p class="lead">Lorem ipsum dolor sit amet, consectetur adipiscing elit, sed do eiusmod tempor incididunt ut labore et dolore magna aliqua. Ut enim ad minim veniam, quis nostrud exercitation ullamco laboris nisi ut aliquip ex ea commodo consequat. Duis aute irure dolor in reprehenderit in voluptate velit</p>
  <a class="btn" href="#">Read More</a>
</section>

<section class="section alt services">
  <div class="mark"></div>
  <h2 class="section-title">What <b>We Do</b></h2>
  <div class="service-list">
    <div class="service">
      <svg viewBox="0 0 100 100" fill="none" stroke="#e3222f" stroke-width="3">
        <rect x="38" y="6" width="24" height="20" rx="2"/>
        <rect x="6" y="56" width="24" height="20" rx="2"/>
        <rect x="70" y="56" width="24" height="20" rx="2"/>
        <line x1="42" y1="28" x2="22" y2="54"/><line x1="58" y1="28" x2="78" y2="54"/>
        <line x1="18" y1="78" x2="18" y2="90"/><line x1="82" y1="78" x2="82" y2="90"/>
        <line x1="18" y1="90" x2="82" y2="90"/>
      </svg>
      <div class="service-name">Organisation design</div>
      <a class="btn" href="#">Read More</a>
    </div>
    <div class="service">
      <svg viewBox="0 0 100 100" fill="none" stroke="#e3222f" stroke-width="3">
        <path d="M46 8h44v30H64l-10 8v-8h-8z"/>
        <line x1="54" y1="18" x2="82" y2="18"/><line x1="54" y1="27" x2="76" y2="27"/>
        <rect x="20" y="58" width="28" height="20" rx="2"/>
        <line x1="4" y1="80" x2="96" y2="80"/><line x1="12" y1="80" x2="12" y2="96"/><line x1="88" y1="80" x2="88" y2="96"/>
      </svg>
      <div class="service-name">Employee Experience</div>
      <a class="btn" href="#">Read More</a>
    </div>
    <div class="service">
      <svg viewBox="0 0 100 100" fill="none" stroke="#e3222f" stroke-width="3">
        <rect x="4" y="24" width="92" height="66" rx="3"/>
        <path d="M36 24V12h28v12"/>
        <line x1="4" y1="52" x2="96" y2="52"/>
        <rect x="44" y="46" width="12" height="12"/>
      </svg>
      <div class="service-name">Change Management</div>
      <a class="btn" href="#">Read More</a>
    </div>
    <div class="service">
      <svg viewBox="0 0 100 100" fill="none" stroke="#e3222f" stroke-width="3">
        <rect x="30" y="8" width="40" height="26" rx="2"/>
        <line x1="50" y1="34" x2="50" y2="50"/>
        <path d="M36 50h28l-4 40H40z"/>
        <line x1="10" y1="92" x2="90" y2="92"/>
      </svg>
      <div class="service-name">Executive Coaching</div>
      <a class="btn" href="#">Read More</a>
    </div>
  </div>
</section>

<section class="section founder">
  <div class="mark"></div>
  <h2 class="section-title">Our <b>Founder</b></h2>
  <p class="lead">Lorem ipsum dolor sit amet, consectetur adipiscing elit, sed do eiusmod tempor incididunt ut labore et dolore magna aliqua. Ut enim ad minim veniam, quis nostrud exercitation ullamco laboris nisi ut aliquip ex ea commodo consequat. Duis aute irure dolor in reprehenderit in voluptate velit</p>
  <div class="portrait" role="img" aria-label="Portrait photograph of the founder in a dark suit"></div>
  <div class="founder-name">Daniel Hart</div>
  <div class="founder-role">Founder</div>
  <a class="btn" href="#">More About Me</a>
</section>

<section class="section alt insights">
  <div class="mark"></div>
  <h2 class="section-title">Insights</h2>
  <p class="lead">Lorem ipsum dolor sit amet, consectetur adipiscing elit, sed do eiusmod tempor incididunt ut labore et dolore magna aliqua. Ut enim ad minim veniam.</p>
  <form class="subscribe">
    <div class="email-field">Enter Email id
      <svg width="12" height="9" viewBox="0 0 12 9"><rect width="12" height="9" fill="#555"/><polyline points="0,0 6,5 12,0" fill="none" stroke="#fff" stroke-width="1"/></svg>
    </div>
    <a class="btn" href="#">Subscribe</a>
  </form>
</section>

<section class="section contact">
  <div class="mark"></div>
  <h2 class="section-title">Contact Us</h2>
  <p class="lead">Lorem ipsum dolor sit amet, consectetur adipiscing elit, sed do eiusmod tempor incididunt ut labore et dolore magna aliqua. Ut enim ad minim veniam.</p>
  <a class="btn" href="#">Get In Touch</a>
</section>

<footer class="site-footer">
  <nav class="footer-nav">
    <a href="#">Home</a><a href="#">The Way We Work</a><a href="#">What We Do</a><a href="#">Our Founder</a><a href="#">Insights</a><a href="#">Contact</a>
  </nav>
  <div class="copyright">&copy; copyright 2018 | www.brightvane.com</div>
  <div class="follow">
    <div class="follow-title">Follow Us</div>
    <div class="social"><span></span><span></span><span></span><span></span></div>
  </div>
</footer>

</body>
</html>
```